new hotel menu

help me do do the graphic design for our country pub the coolabah arms in holbrook. the pub has a relaxed australian country feel. here is a copy of our current menu this has our current logo already on it. the numbers after the dishes and discriptions are the prices as i dont often like to use dollar signs. i will also add a couple of quick files that i hit feeding the menu to word mill. i like the feel but not the results. i will also add a file withthe new menu

```html
<!DOCTYPE html>
<html lang="en">
<head>
<meta charset="utf-8">
<title>The Coolabah Arms – Menu</title>
<link href="https://fonts.googleapis.com/css2?family=Montserrat:wght@300;400;600;700;900&display=swap" rel="stylesheet">
<style>
  :root {
    --page: #ffffff;
    --panel: #e4e1d9;
    --ink: #1f1f1f;
    --ink-soft: #3a3a3a;
    --starters: #7f8f2b;
    --mains: #6b9160;
    --parmi: #dd6419;
    --band-text: #fdf6e3;
    --rule: #2a2a2a;
  }
  * { box-sizing: border-box; margin: 0; padding: 0; }
  html, body { width: 912px; height: 1200px; overflow: hidden; background: var(--page); }
  body { font-family: 'Montserrat', sans-serif; color: var(--ink); }

  .menu-sheet {
    position: absolute; left: 94px; top: 75px; width: 724px; height: 1053px;
    background: var(--panel); overflow: hidden;
  }
  .column-divider {
    position: absolute; left: 359px; top: 0; width: 1.5px; height: 100%;
    background: var(--rule); z-index: 3;
  }

  .landscape-art {
    position: absolute; left: 0; top: 0; width: 359px; height: 125px;
    background: linear-gradient(180deg, #fbf3dc 0%, #f7dcb0 45%, #e6c07a 62%, #a9b84a 80%, #7f8f2b 100%);
  }
  .menu-title {
    position: absolute; left: 25px; top: 12px; font-weight: 900; font-size: 37px;
    letter-spacing: 0.5px; color: var(--ink);
  }

  .band {
    position: absolute; display: flex; justify-content: space-between; align-items: center;
    color: var(--band-text); font-weight: 700;
  }
  .band-title { font-size: 18px; line-height: 1.1; }
  .band-note { font-weight: 400; font-size: 11px; display: block; }
  .band-price { font-size: 15px; line-height: 1.15; }
  .band-starters { left: 0; top: 120px; width: 359px; height: 55px; background: var(--starters); padding: 0 24px 0 27px; }
  .band-parmi { left: 0; top: 687px; width: 362px; height: 55px; background: var(--parmi); padding: 0 20px 0 33px; }
  .band-mains { left: 361px; top: 215px; width: 363px; height: 55px; background: var(--mains); padding: 0 29px 0 27px; }

  .dish { position: absolute; }
  .col-left .dish { left: 27px; width: 312px; }
  .col-right .dish { left: 386px; width: 314px; }
  .dish-name { font-weight: 600; font-size: 16px; line-height: 1.3; }
  .dish-desc { font-weight: 400; font-size: 12px; line-height: 1.45; color: var(--ink-soft); margin-top: 1px; }
  .dish-price { position: absolute; right: 0; top: 0; font-weight: 600; font-size: 16px; }

  .venue-name {
    position: absolute; left: 361px; width: 363px; top: 110px; text-align: center;
    font-weight: 700; font-size: 30px; line-height: 1.15; letter-spacing: 2px; color: var(--ink);
  }

  .outback-art {
    position: absolute; left: 361px; top: 740px; width: 363px; height: 313px; z-index: 0;
    background: linear-gradient(180deg, rgba(228,225,217,0) 0%, #f2d6b0 25%, #efb985 60%, #e9a264 84%, #1a1a1a 86%, #000 100%);
  }
  .col-right .dish { z-index: 1; }
</style>
</head>
<body>
<main class="menu-sheet">
  <div class="landscape-art" role="img" aria-label="Illustrated country landscape with rolling hills, windmill, rider and grazing cattle at sunrise"></div>
  <h1 class="menu-title">MENU</h1>

  <section class="col-left">
    <div class="band band-starters">
      <h2 class="band-title">Starters &amp; Shares<br>and Sides</h2>
      <span class="band-price">price in<br>AUD($)</span>
    </div>

    <div class="dish" style="top:187px"><p class="dish-name">Garlic Bread</p><p class="dish-desc">Classic or with cheese &amp; bacon</p><span class="dish-price">9/12</span></div>
    <div class="dish" style="top:235px"><p class="dish-name">Pumpkin + Feta Arancini</p><p class="dish-desc">sage and pine nut dressing</p><span class="dish-price">15</span></div>
    <div class="dish" style="top:282px"><p class="dish-name">Salt &amp; Pepper Squid</p><p class="dish-desc">With aioli and side salad</p><span class="dish-price">15</span></div>
    <div class="dish" style="top:330px"><p class="dish-name">Fried Prawn Dumplings</p><p class="dish-desc">Soy &amp; sesame dressing</p><span class="dish-price">15</span></div>
    <div class="dish" style="top:377px"><p class="dish-name">Fries- 9 / Loaded 14/<br>parmesan and rosemary salt</p><span class="dish-price">12</span></div>
    <div class="dish" style="top:437px"><p class="dish-name">Bruschetta</p><p class="dish-desc">Tomato, basil, balsamic glaze on<br>toasted garlic loaf</p><span class="dish-price">13</span></div>
    <div class="dish" style="top:501px"><p class="dish-name">Wedges</p><p class="dish-desc">Sour cream &amp; sweet chilli sauce</p><span class="dish-price">13</span></div>
    <div class="dish" style="top:548px"><p class="dish-name">Mashed Potato</p><p class="dish-desc">Creamy butter mash</p><span class="dish-price">05</span></div>
    <div class="dish" style="top:596px"><p class="dish-name">Steamed Veggies</p><p class="dish-desc">Seasonal selection</p><span class="dish-price">06</span></div>
    <div class="dish" style="top:644px"><p class="dish-name">Garden Salad</p><span class="dish-price">06</span></div>

    <div class="band band-parmi">
      <h2 class="band-title">Parmi Menu<span class="band-note">All served with chips &amp; salad or mash &amp; veg</span></h2>
      <span class="band-price">price in<br>AUD($)</span>
    </div>

    <div class="dish" style="top:756px"><p class="dish-name">Classic Parmi</p><p class="dish-desc">Napoli sauce, ham, mozzarella</p><span class="dish-price">28</span></div>
    <div class="dish" style="top:803px"><p class="dish-name">Meat Lovers Parmi</p><p class="dish-desc">BBQ sauce, bacon, pepperoni, ham</p><span class="dish-price">29</span></div>
    <div class="dish" style="top:851px"><p class="dish-name">ABC Parmi</p><p class="dish-desc">Avocado, bacon, cheese</p><span class="dish-price">29</span></div>
    <div class="dish" style="top:899px"><p class="dish-name">Mexican Parmi</p><p class="dish-desc">Salsa, jalapenos, sour cream, cheese</p><span class="dish-price">29</span></div>
    <div class="dish" style="top:946px"><p class="dish-name">Chook on a Hook</p><p class="dish-desc">Topped with a creamy garlic prawn sauce</p><span class="dish-price">32</span></div>
    <div class="dish" style="top:994px"><p class="dish-name">Bushmans</p><p class="dish-desc">mushroom sauce, bacon and cheese</p><span class="dish-price">29</span></div>
  </section>

  <div class="column-divider"></div>

  <section class="col-right">
    <p class="venue-name">THE COOLABAH<br>ARMS</p>

    <div class="band band-mains">
      <h2 class="band-title">Pub Classics<br>&amp; Mains</h2>
      <span class="band-price">price in<br>AUD($)</span>
    </div>

    <div class="outback-art" role="img" aria-label="Sunset outback scene with a silhouetted rider on horseback in front of hazy hills"></div>

    <div class="dish" style="top:288px"><p class="dish-name">Beer-Battered Fish &amp; Chips</p><p class="dish-desc">Gummy shark, house-made beer batter</p><span class="dish-price">24</span></div>
    <div class="dish" style="top:335px"><p class="dish-name">Lamb Cutlets</p><p class="dish-desc">Crumbed, served with mash and steamed greens</p><span class="dish-price">28</span></div>
    <div class="dish" style="top:383px"><p class="dish-name">Scotch Fillet</p><span class="dish-price">39</span></div>
    <div class="dish" style="top:421px"><p class="dish-name" style="font-size:17px">Rump Steak (400g Or 200g)</p><span class="dish-price" style="font-size:17px">39/26</span></div>
    <div class="dish" style="top:463px"><p class="dish-name">Philly Cheesesteak Burger</p><p class="dish-desc" style="margin-top:10px">Grilled sirloin, caramelized onion, swiss cheese,<br>Arms special sauce, Cheese 26</p><span class="dish-price">26</span></div>
    <div class="dish" style="top:541px"><p class="dish-name">Chicken ABC burger Meat</p><p class="dish-desc" style="line-height:1.6">Avocado, bacon, sweet-chilli and cheese<br>with lettuce, sweet chilli mayo</p><span class="dish-price">25</span></div>
    <div class="dish" style="top:609px"><p class="dish-name">Chicken Caesar Salad</p><p class="dish-desc" style="line-height:1.6">Grilled or crispy chicken, bacon, parmesan,<br>caesar dressing</p><span class="dish-price">22</span></div>
    <div class="dish" style="top:677px"><p class="dish-name">Steak sandwich Mexican</p><span class="dish-price">26</span></div>
    <div class="dish" style="top:714px"><p class="dish-name">Prawn and chorizo pasta</p><span class="dish-price" style="top:12px">28</span></div>
    <div class="dish" style="top:750px"><p class="dish-name">Carbonara</p><p class="dish-desc" style="margin-top:5px">Add Chicken 4</p><span class="dish-price" style="top:25px">24</span></div>
    <div class="dish" style="top:815px"><p class="dish-name">Beef and Ironbark Pie</p><span class="dish-price">26</span></div>
    <div class="dish" style="top:852px"><p class="dish-name">Bangers and Mash</p><span class="dish-price">22</span></div>
    <div class="dish" style="top:888px"><p class="dish-name">Roast of the day</p><span class="dish-price">22</span></div>
    <div class="dish" style="top:925px"><p class="dish-name">Barramundi</p><span class="dish-price">30</span></div>
  </section>
</main>
</body>
</html>
```